vantrel works cybersecurity website design and development

website design and development for a cybersecurity company. we have a logo and would like site to suit logo colors and look
cybersecurity website should be secure and look professional
main example of site we want to use: https://www.morvisquad.example/
site should be usable on tablet and phones

For each design proposal, please could you provide details of what language you'll use to code the website.

Target Market(s)

insurance companies, financial institutions, private SME, Africa and Europe

Coding

Coded - Design and coding required

Number of Pages Required

5+ page

Requirements
Must have
• 9 Pages:
Home
About us
Contacts
Partners
Blog
Services
( consulting, vulnerability assessment, information systems security audit, ISO compliance, Penetration testing, security awareness training, social engineering test, protection against DDoS, procurement )
Resources
Technologies
Careers
Nice to have
• nice to have all services have their own pages.
design based on logo colors and look

please provide what will be use to code the website

```html
<!DOCTYPE html>
<html lang="en">
<head>
<meta charset="utf-8">
<title>Vantrel Works – Cybersecurity Consulting</title>
<link rel="stylesheet" href="https://fonts.googleapis.com/css2?family=Poppins:ital,wght@0,400;0,500;0,600;0,700;1,400&family=Roboto:wght@700;900&display=swap">
<style>
:root{
  --blue:#1474d4;
  --blue-dark:#0b3f8f;
  --navy:#07164a;
  --ink:#111111;
  --grey:#555555;
  --white:#ffffff;
}
*{margin:0;padding:0;box-sizing:border-box}
html,body{width:1200px;height:3045px;overflow:hidden;background:var(--white)}
body{position:relative;font-family:"Poppins",sans-serif;color:var(--ink)}
.abs{position:absolute}

/* hero */
.hero-bg{position:absolute;left:0;top:0}
.navbar{left:144px;top:35px;width:912px;height:60px;background:var(--white)}
.brand{position:absolute;left:18px;top:14px;font-size:24px;font-weight:600;color:var(--blue-dark);display:flex;align-items:center;gap:8px;white-space:nowrap}
.brand-dot{width:26px;height:26px;border-radius:50%;background:var(--blue-dark);flex:none}
.nav-link{position:absolute;top:0;height:60px;line-height:60px;font-size:13.5px;color:#333;white-space:nowrap}
.nav-home{position:absolute;left:376px;top:-3px;width:60px;height:68px;background:var(--blue);color:var(--white);font-size:13.5px;display:flex;align-items:center;justify-content:center}
.quote-btn{left:762px;top:15px;width:132px;height:30px;border-radius:15px;background:var(--blue);color:var(--white);font-size:13px;font-weight:600;display:flex;align-items:center;justify-content:center}
.hero-kicker{left:144px;top:234px;font-family:"Roboto",sans-serif;font-weight:900;font-size:47px;color:var(--white);letter-spacing:1px}
.hero-title{left:142px;top:290px;font-family:"Roboto",sans-serif;font-weight:900;font-size:72px;color:var(--white);letter-spacing:1px}
.hero-sub{left:144px;top:372px;font-size:17px;font-weight:500;color:var(--white)}
.btn-outline{left:143px;top:420px;width:180px;height:47px;border-radius:24px;background:var(--blue);border:2px solid var(--white);color:var(--white);font-size:20px;font-weight:500;display:flex;align-items:center;justify-content:center;letter-spacing:1px}
.slide-next{left:839px;top:500px;display:flex;align-items:center;gap:14px;color:var(--white)}
.slide-next .label{font-size:38px;font-weight:300}
.slide-next .num{font-size:66px;font-weight:700;line-height:1}

/* about */
.chameleon{left:508px;top:662px;width:692px;height:615px;background:radial-gradient(ellipse at 60% 55%,#d9dbdf 0%,#eceef1 55%,rgba(255,255,255,0) 75%)}
.section-h{font-family:"Roboto",sans-serif;font-weight:900;font-size:45px;letter-spacing:1px}
.about-h{left:144px;top:768px}
.about-text{left:144px;top:830px;width:462px;font-size:15.5px;line-height:23.2px;color:#222}
.btn-solid{left:144px;top:1111px;width:162px;height:44px;border-radius:22px;background:var(--blue);color:var(--white);font-size:20px;font-weight:500;display:flex;align-items:center;justify-content:center;box-shadow:0 6px 14px rgba(20,116,212,.35);letter-spacing:.5px}
.about-shield{left:654px;top:733px}

/* services */
.services-band{left:0;top:1277px;width:1200px;height:733px;background:linear-gradient(135deg,#0a2b8a 0%,#0d4cb8 45%,#083a93 75%,#0a2a75 100%)}
.services-h{left:0;top:1378px;width:1200px;text-align:center;color:var(--white)}
.service-card{width:285px;height:401px;background:var(--white);overflow:hidden}
.service-photo{height:209px}
.service-card h3{margin-top:26px;text-align:center;font-size:22px;font-weight:600;color:var(--ink)}
.service-card p{margin:12px auto 0;width:250px;text-align:center;font-size:13.5px;line-height:20.5px;color:#444}
.corner{position:absolute;right:0;bottom:0}

/* testimonials */
.testi-deco{left:0;top:2010px;width:1200px;height:560px;background:radial-gradient(ellipse at 40% 20%,#e4e5e8 0%,rgba(255,255,255,0) 55%)}
.testi-h{left:0;top:2090px;width:1200px;text-align:center;font-family:"Roboto",sans-serif;font-weight:700;font-size:45px;color:#333}
.testi-sub{left:0;top:2148px;width:1200px;text-align:center;font-size:16.5px;font-style:italic;color:#555}
.testi-card{top:2194px;width:293px;height:276px;background:var(--white);border:1px solid #e3e6ee;box-shadow:0 2px 10px rgba(0,0,0,.08);text-align:center;color:#555}
.testi-card.featured{background:linear-gradient(180deg,#0f5cc8 0%,#1478d8 100%);color:var(--white);border-color:transparent}
.testi-card p{position:absolute;left:0;right:0;top:26px;margin:0 auto;width:236px;font-size:13px;line-height:19.7px}
.testi-rule{position:absolute;left:124px;top:189px;width:44px;height:2px;background:var(--blue)}
.testi-card.featured .testi-rule{background:var(--white)}
.testi-name{position:absolute;left:0;right:0;top:202px;font-size:21px;font-weight:600;line-height:30px}
.testi-place{position:absolute;left:0;right:0;top:232px;font-size:16px;font-weight:500;line-height:22px}

/* footer */
.footer-bg{left:0;top:2565px}
.footer-brand{left:0;top:2652px;width:1200px;display:flex;justify-content:center;align-items:center;gap:14px;font-size:40px;font-weight:500;color:#5d8fe8}
.footer-brand .brand-dot{width:52px;height:52px;background:#5d8fe8}
.foot-h{font-size:15px;font-weight:600;color:var(--white)}
.foot-contact{left:146px;top:2760px;color:var(--white)}
.contact-row{position:absolute;left:0;display:flex;gap:14px;font-size:14.5px;font-weight:600;line-height:27px;white-space:nowrap}
.contact-row svg{flex:none;margin-top:4px}
.foot-list{list-style:none;font-size:13px;color:var(--white);line-height:29px}
.vline{width:1px;background:rgba(255,255,255,.35)}
.news-input{left:774px;top:2798px;width:282px;height:36px;background:var(--white);border-radius:3px;font-size:14px;color:#888;padding:8px 14px}
.signup{left:777px;top:2850px;width:136px;height:38px;background:var(--blue);border:2px solid var(--white);border-radius:3px;color:var(--white);font-size:18px;display:flex;align-items:center;justify-content:center}
.social{width:28px;height:28px;border:1.5px solid var(--white);border-radius:50%}
.hline{left:144px;top:2981px;width:912px;height:1px;background:rgba(255,255,255,.35)}
.copyright{left:0;top:3006px;width:1200px;text-align:center;font-size:13px;color:var(--white)}
</style>
</head>
<body>

<!-- HERO -->
<svg class="hero-bg" width="1200" height="660" viewBox="0 0 1200 660" role="img" aria-label="Hands typing on a backlit keyboard beside a glowing shield and padlock graphic">
  <defs>
    <linearGradient id="heroGrad" x1="0" y1="0" x2="1" y2="1">
      <stop offset="0" stop-color="#0b1f45"/>
      <stop offset=".45" stop-color="#153a72"/>
      <stop offset="1" stop-color="#0a2456"/>
    </linearGradient>
  </defs>
  <path d="M0 0H1200V547Q600 743 0 547Z" fill="url(#heroGrad)"/>
  <path d="M0 547Q600 743 1200 547" fill="none" stroke="#1474d4" stroke-width="6"/>
</svg>

<header class="abs navbar">
  <div class="brand"><span class="brand-dot"></span>Vantrel Works</div>
  <nav>
    <div class="nav-home">Home</div>
    <a class="nav-link" style="left:453px">About Us</a>
    <a class="nav-link" style="left:537px">Services</a>
    <a class="nav-link" style="left:616px">Blog</a>
    <a class="nav-link" style="left:670px">Contact Us</a>
  </nav>
  <div class="abs quote-btn">Get A Quote</div>
</header>

<div class="abs hero-kicker">WELCOME TO</div>
<h1 class="abs hero-title">VANTREL WORKS</h1>
<div class="abs hero-sub">Cybersecurity Enterprise, Provides Cybersecurity Consulting Services.</div>
<div class="abs btn-outline">Contact Us</div>
<div class="abs slide-next">
  <span class="label">Next</span>
  <svg width="46" height="20" viewBox="0 0 46 20"><path d="M0 10H44M34 1L44 10L34 19" fill="none" stroke="#fff" stroke-width="2.5"/></svg>
  <span class="num">01</span>
</div>
<svg class="abs" style="left:586px;top:566px" width="28" height="62" viewBox="0 0 28 62">
  <rect x="2" y="2" width="24" height="38" rx="12" fill="none" stroke="#fff" stroke-width="2.5"/>
  <circle cx="14" cy="14" r="3" fill="#fff"/>
  <path d="M6 50L14 57L22 50" fill="none" stroke="#fff" stroke-width="2"/>
</svg>

<!-- ABOUT -->
<div class="abs chameleon" role="img" aria-label="Faint grey chameleon resting on a branch"></div>
<h2 class="abs section-h about-h">ABOUT US</h2>
<p class="abs about-text">Lorem Ipsum is simply dummy text of the printing and typesetting industry. Lorem Ipsum has been the industry's standard dummy text ever since the 1500s, when an unknown printer took a galley of type and scrambled it to make a type specimen book. It has survived not only five centuries, but also the leap into electronic typesetting, remaining essentially unchanged. It was popularised in the 1960s with the release of Letraset sheets containing Lorem Ipsum passages, and more recently with desktop publishing software like Aldus PageMaker including versions of Lorem Ipsum.</p>
<div class="abs btn-solid">Read More</div>
<svg class="abs about-shield" width="412" height="463" viewBox="0 0 412 463" role="img" aria-label="Security analysts working at monitors in a server room, framed in a shield">
  <defs>
    <linearGradient id="roomGrad" x1="0" y1="0" x2="0" y2="1">
      <stop offset="0" stop-color="#2a4f86"/>
      <stop offset=".5" stop-color="#1a2f55"/>
      <stop offset="1" stop-color="#0e1a30"/>
    </linearGradient>
  </defs>
  <path d="M6 40Q206 -14 406 40V200Q400 360 206 458Q12 360 6 200Z" fill="#a9d3f0"/>
  <path d="M18 52Q206 4 394 52V202Q388 350 206 444Q24 350 18 202Z" fill="url(#roomGrad)"/>
</svg>

<!-- WHAT WE DO -->
<div class="abs services-band" role="img" aria-label="Deep blue background with a network line pattern"></div>
<h2 class="abs section-h services-h">WHAT WE DO</h2>

<article class="abs service-card" style="left:145px;top:1499px">
  <div class="service-photo" role="img" aria-label="Two colleagues reviewing work at a laptop" style="background:linear-gradient(135deg,#eef0f2,#b9bcc2 60%,#6a6c72)"></div>
  <h3>Consulting</h3>
  <p>Lorem Ipsum is simply dummy text of the printing and typesetting industry. Lorem Ipsum has been the industry's standard dummy text ever</p>
  <svg class="corner" width="56" height="56" viewBox="0 0 56 56"><path d="M56 0V56H0Z" fill="#0b3f8f"/><path d="M22 40H46M40 34L46 40L40 46" fill="none" stroke="#fff" stroke-width="2"/></svg>
</article>

<article class="abs service-card" style="left:457px;top:1467px">
  <div class="service-photo" role="img" aria-label="Hand touching a tablet with glowing financial charts" style="background:linear-gradient(135deg,#dfe3ea,#8a97ad 55%,#c98a3c)"></div>
  <h3>Financial Organisations</h3>
  <p>Lorem Ipsum is simply dummy text of the printing and typesetting industry. Lorem Ipsum has been the industry's standard dummy text ever</p>
  <svg class="corner" width="56" height="56" viewBox="0 0 56 56"><path d="M56 0V56H0Z" fill="#1474d4"/><path d="M22 40H46M40 34L46 40L40 46" fill="none" stroke="#fff" stroke-width="2"/></svg>
</article>

<article class="abs service-card" style="left:769px;top:1499px">
  <div class="service-photo" role="img" aria-label="Glowing neon circuit board tower" style="background:linear-gradient(135deg,#0b1240,#2d3fb0 50%,#b02a9c)"></div>
  <h3>Fintech</h3>
  <p>Lorem Ipsum is simply dummy text of the printing and typesetting industry. Lorem Ipsum has been the industry's standard dummy text ever</p>
  <svg class="corner" width="56" height="56" viewBox="0 0 56 56"><path d="M56 0V56H0Z" fill="#0b3f8f"/><path d="M22 40H46M40 34L46 40L40 46" fill="none" stroke="#fff" stroke-width="2"/></svg>
</article>

<!-- TESTIMONIALS -->
<div class="abs testi-deco" role="img" aria-label="Faint grey chameleon outline"></div>
<h2 class="abs testi-h">Testimonials</h2>
<p class="abs testi-sub">Neque porro quisquam est qui dolorem ipsum quia dolor sit amet, consectetur, adipisci velit.</p>

<article class="abs testi-card" style="left:145px">
  <p>"Lorem Ipsum is simply dummy text of the printing and typesetting industry. Lorem Ipsum has been the industry's standard dummy text ever since the 1500s, when an unknown printer took a galley of type and scrambled it to make a type specimen book. It</p>
  <div class="testi-rule"></div>
  <div class="testi-name">Elias R Brant</div>
  <div class="testi-place">California</div>
</article>
<article class="abs testi-card featured" style="left:454px">
  <p>Lorem Ipsum is simply dummy text of the printing and typesetting industry. Lorem Ipsum has been the industry's standard dummy text ever since the 1500s, when an unknown printer took a galley of type and scrambled it to make a type specimen book. It</p>
  <div class="testi-rule"></div>
  <div class="testi-name">Nora T Halvik</div>
  <div class="testi-place">Florida</div>
</article>
<article class="abs testi-card" style="left:761px">
  <p>Lorem Ipsum is simply dummy text of the printing and typesetting industry. Lorem Ipsum has been the industry's standard dummy text ever since the 1500s, when an unknown printer took a galley of type and scrambled it to make a type specimen book. It</p>
  <div class="testi-rule"></div>
  <div class="testi-name">Marcus L Perrin</div>
  <div class="testi-place">North Carolina</div>
</article>

<!-- FOOTER -->
<svg class="abs footer-bg" width="1200" height="480" viewBox="0 0 1200 480" role="img" aria-label="Dark navy background with faint network lines and red glow">
  <defs>
    <radialGradient id="footGrad" cx=".15" cy=".95" r="1">
      <stop offset="0" stop-color="#3a1040"/>
      <stop offset=".35" stop-color="#0c1c5c"/>
      <stop offset="1" stop-color="#06113d"/>
    </radialGradient>
  </defs>
  <path d="M0 100Q600 -100 1200 100V480H0Z" fill="url(#footGrad)"/>
</svg>

<div class="abs footer-brand"><span class="brand-dot"></span>Vantrel Works</div>

<div class="abs foot-h" style="left:146px;top:2762px">Contact Us</div>
<div class="abs foot-contact">
  <div class="contact-row" style="top:46px">
    <svg width="20" height="20" viewBox="0 0 24 24"><path d="M6.6 10.8a15 15 0 0 0 6.6 6.6l2.2-2.2a1 1 0 0 1 1-.25 11.4 11.4 0 0 0 3.6.57 1 1 0 0 1 1 1V20a1 1 0 0 1-1 1A17 17 0 0 1 3 4a1 1 0 0 1 1-1h3.5a1 1 0 0 1 1 1c0 1.25.2 2.45.57 3.6a1 1 0 0 1-.25 1z" fill="#1e88e5"/></svg>
    <span>Phone: +828-555-0142</span>
  </div>
  <div class="contact-row" style="top:82px">
    <svg width="20" height="20" viewBox="0 0 24 24"><path d="M2 5h20v14H2z" fill="#1e88e5"/><path d="M2 5l10 8 10-8" fill="none" stroke="#06113d" stroke-width="1.6"/></svg>
    <span>Email:&nbsp; hi@vantrel.example</span>
  </div>
  <div class="contact-row" style="top:122px">
    <svg width="20" height="24" viewBox="0 0 24 28"><path d="M12 1a9 9 0 0 0-9 9c0 7 9 17 9 17s9-10 9-17a9 9 0 0 0-9-9zm0 12.5A3.5 3.5 0 1 1 12 6.5a3.5 3.5 0 0 1 0 7z" fill="#1e88e5"/></svg>
    <span>418&nbsp; Calder Row,<br>North Carolina, 28790.</span>
  </div>
</div>

<div class="abs vline" style="left:411px;top:2778px;height:200px"></div>
<div class="abs foot-h" style="left:431px;top:2763px">Quick Links</div>
<ul class="abs foot-list" style="left:431px;top:2794px">
  <li>Home</li><li>About Us</li><li>Services</li><li>Blog</li><li>Contact Us</li>
</ul>
<div class="abs vline" style="left:547px;top:2790px;height:190px"></div>
<div class="abs foot-h" style="left:579px;top:2763px">Services</div>
<ul class="abs foot-list" style="left:579px;top:2794px">
  <li>Cybersecurity Consulting</li><li>Financial Organisations</li><li>Fintech</li>
</ul>
<div class="abs vline" style="left:748px;top:2778px;height:200px"></div>
<div class="abs foot-h" style="left:770px;top:2763px">Sign up for newsletter</div>
<div class="abs news-input">Your Email</div>
<div class="abs signup">SIGN UP</div>
<div class="abs social" style="left:771px;top:2913px"></div>
<div class="abs social" style="left:803px;top:2913px"></div>
<div class="abs social" style="left:836px;top:2913px"></div>
<div class="abs social" style="left:868px;top:2913px"></div>

<div class="abs hline"></div>
<div class="abs copyright">Vantrel Works © 2021 All Rights Reserved. |&nbsp; Privacy Policy</div>

</body>
</html>
```